Cadenza Elite Keyboard Academy is a comprehensive piano studio located in CBD area and provide individual piano lessons.

We also provide services for wedding organising band, or instrumental hiring or venue hiring, or organise concert to students.

I want my name card to be very creative, does not have to be the form or shape with the normal name card, can be in different shape. Also, I want the name card to be very upper class, because learning piano is a serious thing, so I do not want people to bargain with the prices. I want people to see it as a very elegant tuition so that they do not want to bargain and think it is worth to try.

Further more, Cadenza Elite Keyboard Academy is not like normal piano studio only provide piano lessons, we provide band services for each other event, such as cruise party, wedding etc. I want people to see it as owner of Elite Keyboard Academy, they will have different type of services all in one, I provide more than that, and I am well connected. I do not provide only piano lesson, but also all other musical knowledge and I am very professional

I want name card to be very simple, just name of company name, my name and website that's all, maybe phone number and email as well.

Please check my website to have more ideal concept.
http://harrietdowse.sitebuilder-example.com/cadenzakeyboard
Updates

Target Market(s)

For all people who love to play piano (better with upper class)

Industry/Entity Type

Wedding

Contact Information for Business Card

Harriet Dowse
Mobile:0418769052
Email: cadenzaelitekeys@mailbox-example.com

Colors

Designer to choose colors to be used in the design.

Requirements
Must have
• Creativity
Nice to have
• Black and white
some sort of piano image
Should not have
• Childish

```html
<!DOCTYPE html>
<html lang="en">
<head>
<meta charset="utf-8">
<title>Cadenza Elite Keyboard Academy — Business Card</title>
<link rel="stylesheet" href="https://fonts.googleapis.com/css2?family=Bodoni+Moda:wght@400;600&display=swap">
<style>
  :root {
    --backdrop: #8a5430;
    --card-white: #ffffff;
    --card-black: #2b2b2b;
    --ink: #1a1a1a;
    --paper-ink: #f4f4f4;
    --frame-dark: #222222;
    --frame-light: #fafafa;
    --art-tone: #d9d9d9;
  }
  * { margin: 0; padding: 0; box-sizing: border-box; }
  html, body {
    width: 1200px;
    height: 841px;
    overflow: hidden;
    background: var(--backdrop);
  }
  .canvas {
    position: relative;
    width: 1200px;
    height: 841px;
    display: flex;
    justify-content: center;
    align-items: center;
    gap: 110px;
  }
  .card {
    width: 380px;
    height: 620px;
    position: relative;
    font-family: "Bodoni Moda", "Didot", serif;
    box-shadow: 0 6px 18px rgba(0,0,0,0.35);
  }
  .card--front {
    background: var(--card-white);
    border: 7px solid var(--frame-dark);
    color: var(--ink);
    display: flex;
    flex-direction: column;
    align-items: center;
  }
  .piano-art {
    margin-top: 140px;
    width: 210px;
    height: 185px;
    background: linear-gradient(135deg, var(--art-tone), #f2f2f2);
  }
  .contact {
    margin-top: auto;
    margin-bottom: 34px;
    text-align: center;
    width: 100%;
    padding: 0 14px;
  }
  .contact__name {
    font-size: 34px;
    font-weight: 400;
    margin-bottom: 20px;
  }
  .contact__line {
    font-size: 15px;
    line-height: 1.45;
  }
  .contact__line--small {
    font-size: 11px;
    letter-spacing: -0.1px;
  }
  .card--back {
    background: var(--card-black);
    border: 7px solid var(--frame-light);
    color: var(--paper-ink);
    display: flex;
    align-items: center;
    justify-content: center;
  }
  .studio-name {
    text-align: center;
    font-size: 50px;
    font-weight: 600;
    line-height: 1.32;
    margin-top: -40px;
  }
</style>
</head>
<body>
  <main class="canvas">
    <section class="card card--front">
      <div class="piano-art" role="img" aria-label="Line drawing of a grand piano with raised lid"></div>
      <div class="contact">
        <h1 class="contact__name">Harriet Dowse</h1>
        <p class="contact__line">mob: 0418 769 052</p>
        <p class="contact__line contact__line--small">email: cadenzaelitekeys@mailbox-example.com</p>
        <p class="contact__line contact__line--small">http://harrietdowse.sitebuilder-example.com/cadenzakeyboard</p>
      </div>
    </section>
    <section class="card card--back">
      <h2 class="studio-name">Cadenza<br>Elite<br>Keyboard<br>Academy</h2>
    </section>
  </main>
</body>
</html>
```